Brackwell Immigration Law

We need a web design for our existing company www.brackwellcounsel.co.uk. We are an immigration consultancy. The final design should communicate professionalism, integrity and affordability.

Industry/Entity Type

It Company

Logo Text

Brackwell Counsel Partners

Number of Pages Required

5+ page

Font styles to use
Serif

Requirements
Must have
• I want to have the same silhouette logo but something different in positioning..
Nice to have
• Please have a look at these websites:
• https://www.travelpathguide.co.uk/visa_uk/
• http://www.oakdenadvisers.co.uk/
• http://www.myrtlegatelaw.org/index.php
• www.brackwellcounsel.co.uk

```html
<!DOCTYPE html>
<html lang="en">
<head>
<meta charset="utf-8">
<title>Brackwell Counsel Partners – Immigration Law</title>
<link rel="stylesheet" href="https://fonts.googleapis.com/css2?family=Open+Sans:wght@400;600;700&family=Oswald:wght@400;500&display=swap">
<style>
:root{
  --red:#c8202a;
  --ink:#2b2b2b;
  --text:#555;
  --muted:#888;
  --topbar:#262626;
  --footer:#2a2a2a;
  --footer-line:#444;
  --band:#ececec;
  --navy:#24446f;
  --white:#fff;
}
*{box-sizing:border-box;margin:0;padding:0}
html,body{width:1200px;height:2404px;overflow:hidden}
body{font-family:"Open Sans",Arial,sans-serif;color:var(--text);background:var(--white);position:relative;font-size:13px;line-height:1.6}
a{color:inherit;text-decoration:none}
.read-more{color:var(--red);font-size:12px;font-weight:600}

.topbar{height:32px;background:var(--topbar);display:flex;justify-content:flex-end;align-items:center;gap:28px;padding-right:40px;color:#ddd;font-size:12px}
.topbar span{display:flex;align-items:center;gap:8px}

.header{height:98px;display:flex;align-items:center;justify-content:space-between;padding:0 20px 0 30px;border-bottom:1px solid #e5e5e5}
.logo{display:flex;align-items:center;gap:12px}
.logo-mark{width:34px;height:34px;background:var(--ink)}
.logo-name{font-weight:700;color:var(--ink);font-size:17px;letter-spacing:1px;line-height:1.15;width:180px}
.nav{display:flex;height:98px}
.nav a{width:104px;display:flex;flex-direction:column;align-items:center;justify-content:center;gap:8px;color:var(--ink);font-size:13px;font-weight:600}
.nav a.active{background:var(--red);color:var(--white)}

.hero{position:absolute;top:130px;left:0;width:1200px;height:470px;background:linear-gradient(120deg,#d99aa7 0%,#c3526a 25%,#e8e2e2 45%,#2c3f66 65%,#1b2745 80%,#d9d4d2 100%)}
.hero-caption{position:absolute;left:60px;bottom:70px;font-family:"Oswald",sans-serif;font-size:34px;font-weight:500;color:var(--white);letter-spacing:.5px}
.slide-arrow{position:absolute;top:200px;width:40px;height:40px;border-radius:50%;background:rgba(0,0,0,.45);display:flex;align-items:center;justify-content:center}

.assessment{position:absolute;top:566px;left:820px;width:360px;height:160px;background:var(--white);box-shadow:0 2px 10px rgba(0,0,0,.25)}
.assessment-head{display:flex;gap:12px;padding:14px 16px;height:70px}
.assessment-icon{width:36px;height:36px;background:var(--navy)}
.assessment h3{font-size:18px;color:var(--ink);font-weight:700;line-height:1.2}
.assessment p{font-size:11px;color:var(--muted)}
.assessment-body{background:#e9e9e9;height:90px;padding:22px 16px}
.select{height:38px;background:var(--white);border:1px solid #ccc;display:flex;align-items:center;justify-content:space-between;padding:0 12px;font-size:12px;color:var(--muted)}

.welcome{position:absolute;top:612px;left:60px;width:730px}
.welcome h2{font-size:22px;color:var(--ink);font-weight:700;margin-bottom:12px}
.welcome p{margin-bottom:10px;font-size:12px}

.section-head{display:flex;justify-content:space-between;align-items:center;border-bottom:1px solid #ddd;padding-bottom:10px}
.section-head h2{font-size:22px;color:var(--ink);font-weight:700}
.arrows{display:flex;gap:6px}
.arrows span{width:26px;height:26px;background:#555;display:flex;align-items:center;justify-content:center}

.services{position:absolute;top:868px;left:48px;width:1104px}
.cards{display:flex;gap:42px;margin-top:26px}
.card{width:340px}
.card-photo{height:190px;margin-bottom:12px}
.card h3{font-size:17px;color:var(--ink);font-weight:700;margin-bottom:4px}
.card p{font-size:12px;margin-bottom:6px}

.blog{position:absolute;top:1272px;left:0;width:1200px;height:548px;background:var(--band);padding:22px 48px 0}
.blog-grid{display:grid;grid-template-columns:552px 552px;grid-template-rows:205px 245px;margin-top:18px}
.post{padding:20px 24px;background:var(--white)}
.post.feature{background:var(--navy);color:#d7e0ee}
.post h3{font-size:22px;font-weight:600;color:var(--ink);line-height:1.3;margin-bottom:6px}
.post.feature h3{color:var(--white)}
.post .meta{font-size:11px;color:var(--red);margin-bottom:8px}
.post.feature .meta{color:#a9c0e0}
.post p{font-size:12px;margin-bottom:8px}

.subscribe{position:absolute;top:1820px;left:0;width:1200px;height:280px;background:linear-gradient(180deg,#3a3a3a,#5a5050 50%,#2e2e2e);text-align:center;color:var(--white)}
.subscribe h2{font-size:24px;font-weight:600;margin-top:100px;letter-spacing:1px}
.subscribe p{font-size:12px;color:#ddd}
.subscribe-form{display:flex;justify-content:center;gap:18px;margin-top:24px}
.field{width:330px;height:38px;background:var(--white);color:#999;font-size:12px;text-align:left;padding:10px 14px}
.submit{width:110px;height:38px;background:var(--red);color:var(--white);font-weight:700;font-size:13px;line-height:38px}

.footer{position:absolute;top:2100px;left:0;width:1200px;height:280px;background:var(--footer);color:#ccc;display:flex;padding:22px 30px 0;gap:40px}
.footer h4{color:var(--white);font-size:17px;font-weight:600;padding-bottom:8px;border-bottom:1px solid var(--footer-line);margin-bottom:14px}
.col-links{width:240px}
.col-contact{width:280px}
.col-map{width:320px}
.col-social{width:220px}
.footer li{list-style:none;font-size:12px;line-height:1.9;padding-left:14px;position:relative}
.footer li::before{content:"";position:absolute;left:0;top:10px;width:5px;height:5px;background:var(--red)}
.contact-row{display:flex;gap:12px;font-size:12px;margin-bottom:10px;line-height:1.5}
.map{height:150px;background:linear-gradient(135deg,#3c3c3c,#555)}
.social{display:flex;align-items:center;gap:12px;font-size:12px;margin-bottom:12px}
.social i{width:24px;height:24px;display:block}

.copyright{position:absolute;top:2380px;left:0;width:1200px;height:24px;background:#1c1c1c;color:#999;font-size:11px;text-align:center;line-height:24px}
</style>
</head>
<body>

<div class="topbar">
  <span><svg width="14" height="10" viewBox="0 0 14 10"><rect x=".5" y=".5" width="13" height="9" fill="none" stroke="#ddd"/><path d="M.5 .5 7 6 13.5 .5" fill="none" stroke="#ddd"/></svg>info@brackwellcounsel.co.uk</span>
  <span><svg width="10" height="14" viewBox="0 0 10 14"><rect x=".5" y=".5" width="9" height="13" rx="1.5" fill="none" stroke="#ddd"/><circle cx="5" cy="11" r="1" fill="#ddd"/></svg>07400 555 012</span>
</div>

<header class="header">
  <div class="logo"><span class="logo-mark"></span><span class="logo-name">BRACKWELL COUNSEL PARTNERS</span></div>
  <nav class="nav">
    <a class="active" href="#"><svg width="22" height="20" viewBox="0 0 22 20"><path d="M2 10 11 2l9 8M5 8v10h12V8" fill="none" stroke="currentColor" stroke-width="2"/></svg>Home</a>
    <a href="#"><svg width="22" height="20" viewBox="0 0 22 20"><rect x="2" y="6" width="18" height="12" fill="none" stroke="currentColor" stroke-width="2"/><path d="M8 6V3h6v3" fill="none" stroke="currentColor" stroke-width="2"/></svg>Work Visas</a>
    <a href="#"><svg width="22" height="20" viewBox="0 0 22 20"><circle cx="7" cy="6" r="3" fill="currentColor"/><circle cx="15" cy="6" r="3" fill="currentColor"/><path d="M2 18c0-5 10-5 10 0M10 18c0-5 10-5 10 0" fill="currentColor"/></svg>Family Visas</a>
    <a href="#"><svg width="22" height="20" viewBox="0 0 22 20"><rect x="4" y="2" width="14" height="16" fill="none" stroke="currentColor" stroke-width="2"/><path d="M8 6h2M12 6h2M8 10h2M12 10h2" stroke="currentColor" stroke-width="2"/></svg>Business Visas</a>
    <a href="#"><svg width="22" height="20" viewBox="0 0 22 20"><path d="M1 7 11 2l10 5-10 5z" fill="currentColor"/><path d="M5 10v5c3 3 9 3 12 0v-5" fill="none" stroke="currentColor" stroke-width="2"/></svg>Student Visas</a>
    <a href="#"><svg width="22" height="20" viewBox="0 0 22 20"><circle cx="11" cy="10" r="8" fill="none" stroke="currentColor" stroke-width="2"/><path d="M11 9v5M11 6v1" stroke="currentColor" stroke-width="2"/></svg>About us</a>
    <a href="#"><svg width="22" height="20" viewBox="0 0 22 20"><circle cx="11" cy="10" r="8" fill="none" stroke="currentColor" stroke-width="2"/><path d="M11 6v8M7 10h8" stroke="currentColor" stroke-width="2"/></svg>Join Us</a>
    <a href="#"><svg width="22" height="20" viewBox="0 0 22 20"><rect x="2" y="4" width="18" height="12" fill="none" stroke="currentColor" stroke-width="2"/><path d="M2 4l9 7 9-7" fill="none" stroke="currentColor" stroke-width="2"/></svg>Contact Us</a>
  </nav>
</header>

<section class="hero" role="img" aria-label="Photo of a traveller holding a dark blue passport">
  <span class="slide-arrow" style="left:10px"><svg width="12" height="16" viewBox="0 0 12 16"><path d="M9 2 3 8l6 6" fill="none" stroke="#fff" stroke-width="2"/></svg></span>
  <span class="slide-arrow" style="right:10px"><svg width="12" height="16" viewBox="0 0 12 16"><path d="M3 2l6 6-6 6" fill="none" stroke="#fff" stroke-width="2"/></svg></span>
  <h1 class="hero-caption">PROVIDING ASSISTANCE REGARDING IMMIGRATION</h1>
</section>

<section class="welcome">
  <h2>WELCOME TO BRACKWELL COUNSEL PARTNERS</h2>
  <p>Lorem ipsum dolor sit amet, consectetuer adipiscing elit, sed diam nonummy nibh euismod tincidunt ut laoreet dolore magna aliquam erat volutpat. Ut wisi enim ad minim veniam, quis nostrud exerci tation ullamcorper suscipit lobortis nisl ut aliquip ex ea commodo consequat. Duis autem vel eum iriure dolor in hendrerit in vulputate velit esse molestie consequat.</p>
  <p>Ut wisi enim ad minim veniam, quis nostrud exerci tation ullamcorper suscipit lobortis nisl ut aliquip ex ea commodo consequat. Duis autem vel eum iriure dolor in hendrerit in vulputate velit esse molestie consequat, vel illum dolore eu feugiat nulla facilisis.</p>
  <a class="read-more" href="#">Read More</a>
</section>

<aside class="assessment">
  <div class="assessment-head">
    <span class="assessment-icon"></span>
    <div><h3>VISA ASSESSMENT</h3><p>What's the best Visa for you?</p></div>
  </div>
  <div class="assessment-body">
    <div class="select">Select Visa Types <svg width="10" height="6" viewBox="0 0 10 6"><path d="M0 0h10L5 6z" fill="#888"/></svg></div>
  </div>
</aside>

<section class="services">
  <div class="section-head"><h2>SERVICES</h2>
    <div class="arrows"><span><svg width="8" height="12" viewBox="0 0 8 12"><path d="M6 1 1 6l5 5" fill="none" stroke="#fff" stroke-width="2"/></svg></span><span><svg width="8" height="12" viewBox="0 0 8 12"><path d="M2 1l5 5-5 5" fill="none" stroke="#fff" stroke-width="2"/></svg></span></div>
  </div>
  <div class="cards">
    <article class="card"><div class="card-photo" role="img" aria-label="Photo of business professionals standing in a row" style="background:linear-gradient(180deg,#8fb6d8,#2f3e52)"></div><h3>Work Visa</h3><p>Lorem ipsum dolor sit amet, consectetuer adipiscing elit, sed diam nonummy nibh euismod tincidunt. Duis autem vel eum iriure dolor in hendrerit in vulputate.</p><a class="read-more" href="#">Read More</a></article>
    <article class="card"><div class="card-photo" role="img" aria-label="Photo of a smiling family outdoors" style="background:linear-gradient(180deg,#c9b79a,#6f5a44)"></div><h3>Family Visa</h3><p>Lorem ipsum dolor sit amet, consectetuer adipiscing elit, sed diam nonummy nibh euismod tincidunt. Duis autem vel eum iriure dolor in hendrerit in vulputate.</p><a class="read-more" href="#">Read More</a></article>
    <article class="card"><div class="card-photo" role="img" aria-label="Photo of a businessman in a suit" style="background:linear-gradient(180deg,#dcdcdc,#4a4a52)"></div><h3>Business Visa</h3><p>Lorem ipsum dolor sit amet, consectetuer adipiscing elit, sed diam nonummy nibh euismod tincidunt. Duis autem vel eum iriure dolor in hendrerit in vulputate.</p><a class="read-more" href="#">Read More</a></article>
  </div>
</section>

<section class="blog">
  <div class="section-head"><h2>RECENT BLOGS POSTS</h2>
    <div class="arrows"><span><svg width="8" height="12" viewBox="0 0 8 12"><path d="M6 1 1 6l5 5" fill="none" stroke="#fff" stroke-width="2"/></svg></span><span><svg width="8" height="12" viewBox="0 0 8 12"><path d="M2 1l5 5-5 5" fill="none" stroke="#fff" stroke-width="2"/></svg></span></div>
  </div>
  <div class="blog-grid">
    <article class="post"><h3>Lorem ipsum dolor sit amet, consectetuer</h3><div class="meta">Posted: July 24, 2015 &nbsp;|&nbsp; 11 Comments</div><p>Lorem ipsum dolor sit amet, consectetuer adipiscing elit, sed diam nonummy nibh euismod tincidunt ut laoreet dolore magna aliquam erat volutpat. Ut wisi enim ad minim veniam, quis nostrud exerci tation ullamcorper suscipit lobortis.</p><a class="read-more" href="#">Read More</a></article>
    <div role="img" aria-label="Photo of colleagues meeting in a bright office" style="background:linear-gradient(135deg,#e4e1dc,#8a9aae)"></div>
    <div role="img" aria-label="Photo of a consultant advising a client across a desk" style="background:linear-gradient(135deg,#b9a48c,#4c4a55)"></div>
    <article class="post feature" style="padding-top:60px"><h3>Lorem ipsum dolor sit amet, consectetuer</h3><div class="meta">Posted: July 24, 2015 &nbsp;|&nbsp; 11 Comments</div><p>Lorem ipsum dolor sit amet, consectetuer adipiscing elit, sed diam nonummy nibh euismod tincidunt ut laoreet dolore magna aliquam erat volutpat. Ut wisi enim ad minim veniam, quis nostrud exerci tation ullamcorper.</p><a class="read-more" href="#" style="color:#fff">Read More</a></article>
  </div>
</section>

<section class="subscribe" role="img" aria-label="Dark photo background of a person at a desk">
  <h2>A SUBSCRIPTION BOX</h2>
  <p>Lorem ipsum dolor sit amet, consectetuer adipiscing elit. Donec non vulputate dui.</p>
  <div class="subscribe-form"><div class="field">Enter Name</div><div class="field">Enter Email</div><div class="submit">SUBMIT</div></div>
</section>

<footer class="footer">
  <div class="col-links"><h4>Quick Links</h4><ul><li>Home</li><li>About Us</li><li>Join Us</li><li>Contact Us</li><li>Blog</li><li>Contact Us</li></ul></div>
  <div class="col-contact"><h4>Contact Us</h4>
    <div class="contact-row"><svg width="12" height="16" viewBox="0 0 12 16"><path d="M6 15C2 9 1 7 1 5.5a5 5 0 0 1 10 0C11 7 10 9 6 15z" fill="#ccc"/><circle cx="6" cy="5.5" r="2" fill="#2a2a2a"/></svg><span><b style="color:#fff">Brackwell Counsel Partners</b><br>48 Harwell Row<br>London EC1 4QT</span></div>
    <div class="contact-row"><svg width="12" height="14" viewBox="0 0 12 14"><rect x="1" y="1" width="10" height="12" rx="2" fill="#ccc"/></svg><span>0207 555 0193</span></div>
    <div class="contact-row"><svg width="14" height="10" viewBox="0 0 14 10"><rect x=".5" y=".5" width="13" height="9" fill="none" stroke="#ccc"/><path d="M.5 .5 7 6 13.5 .5" fill="none" stroke="#ccc"/></svg><span>info@brackwellcounsel.co.uk</span></div>
  </div>
  <div class="col-map"><h4>Location</h4><div class="map" role="img" aria-label="World map showing office location"></div></div>
  <div class="col-social"><h4>Follow Us On</h4>
    <div class="social"><i style="background:#3b5a98"></i>Social Feed</div>
    <div class="social"><i style="background:#3aa2dc"></i>Short Posts</div>
    <div class="social"><i style="background:#d3302a"></i>Video Channel</div>
    <div class="social"><i style="background:#1e6ea8"></i>Career Network</div>
  </div>
</footer>

<div class="copyright">©Brackwell Counsel Partners 2015. All Rights Reserved.</div>
</body>
</html>
```